Bright Meadow Sausage Co. (This is a gourmet hot dog restaurant concept)

Need a Restaurant Signage.
Name of the restaurant: Bright Meadow Sausage Co.

The restaurant will feature Hot Dogs which customers can customize with Toppings and Relishes. Customers will be able to choose their Frank, Toppings and Relish. Making their "personal" hot dog. It will feature toppings from various states in the USA and also around the world.

The Sign Needs to be linear. I will need details for my signage shop including Fonts, Colors Specifications

Target Market(s)

Restaurants

Industry/Entity Type

Restaurant

Colors

Designer to choose colors to be used in the design.

Requirements
Must have
• Unique, easy to understand and fun
Nice to have
• Be creative
Should not have
• Not Complicated and confusing

```html
<!DOCTYPE html>
<html lang="en">
<head>
<meta charset="utf-8">
<title>Bright Meadow Sausage Co. — Hot &amp; Personal</title>
<link rel="stylesheet" href="https://fonts.googleapis.com/css2?family=Anton&family=Jost:wght@400;500&family=Montserrat:wght@700&display=swap">
<style>
  :root {
    --paper: #f3f3f4;
    --paper-shade: #e4e5e8;
    --headline-blue: #2f4a8e;
    --headline-navy: #1f253f;
    --accent-red: #e3323a;
    --band-red: #e0343a;
    --band-deep: #5b2a2d;
    --bun-light: #e2a76f;
    --bun-dark: #a8683a;
    --white: #ffffff;
  }
  * { box-sizing: border-box; margin: 0; padding: 0; }
  html, body { width: 900px; height: 1200px; overflow: hidden; }
  body { background: var(--paper); }

  .sign {
    position: relative;
    width: 900px;
    height: 1200px;
    overflow: hidden;
    background:
      linear-gradient(to bottom,
        var(--paper) 0px,
        var(--paper-shade) 540px,
        var(--band-red) 600px,
        #c22f36 820px,
        var(--band-deep) 1200px);
  }

  .headline {
    position: absolute;
    left: 44px;
    top: 66px;
    font-family: "Anton", "Oswald", sans-serif;
    text-transform: uppercase;
    line-height: 0.9;
  }
  .headline__word {
    display: inline-block;
    font-size: 150px;
    letter-spacing: 1px;
    background: linear-gradient(to bottom, var(--headline-blue) 50%, var(--headline-navy) 50%);
    -webkit-background-clip: text;
    background-clip: text;
    color: transparent;
  }
  .headline__amp {
    display: inline-block;
    font-family: "Montserrat", sans-serif;
    font-weight: 700;
    font-size: 62px;
    color: var(--accent-red);
    vertical-align: 14px;
    margin-left: 10px;
  }

  .brand {
    position: absolute;
    right: 36px;
    top: 92px;
    width: 230px;
    display: flex;
    align-items: center;
    gap: 12px;
  }
  .brand__dot {
    flex: none;
    width: 26px;
    height: 26px;
    border-radius: 50%;
    background: var(--accent-red);
  }
  .brand__name {
    font-family: "Jost", sans-serif;
    font-weight: 500;
    font-size: 30px;
    line-height: 1.12;
    color: var(--headline-navy);
  }

  .hero-art {
    position: absolute;
    left: 0;
    top: 300px;
    width: 900px;
    height: 620px;
  }

  .contact {
    position: absolute;
    left: 51px;
    top: 978px;
    width: 798px;
    height: 96px;
    border: 3px solid var(--white);
    display: flex;
    align-items: center;
    justify-content: center;
  }
  .contact__label {
    position: absolute;
    top: -34px;
    left: 50%;
    transform: translateX(-50%);
    padding: 0 22px;
    background: #b22e34;
    font-family: "Jost", sans-serif;
    font-weight: 400;
    font-size: 46px;
    line-height: 1.3;
    color: var(--white);
    white-space: nowrap;
    background: linear-gradient(to bottom, #b52f35, #ad2e34);
  }
  .contact__phone {
    margin-top: 14px;
    font-family: "Montserrat", sans-serif;
    font-weight: 700;
    font-size: 56px;
    color: var(--white);
    letter-spacing: 0.5px;
    white-space: nowrap;
  }

  .website {
    position: absolute;
    left: 0;
    width: 900px;
    top: 1120px;
    display: flex;
    align-items: center;
    justify-content: center;
    gap: 8px;
    font-family: "Jost", sans-serif;
    font-size: 26px;
    color: var(--white);
  }
  .website__icon { width: 26px; height: 26px; }
</style>
</head>
<body>
  <main class="sign">
    <h1 class="headline">
      <span class="headline__word">Hot</span><span class="headline__amp">&amp;</span><br>
      <span class="headline__word">Personal</span>
    </h1>

    <div class="brand">
      <span class="brand__dot"></span>
      <span class="brand__name">Bright Meadow Sausage Co.</span>
    </div>

    <svg class="hero-art" viewBox="0 0 900 620" role="img" aria-label="Illustration of a large hot dog in a sesame bun with a mustard zigzag">
      <defs>
        <linearGradient id="bunTone" x1="0" y1="0" x2="0" y2="1">
          <stop offset="0" stop-color="var(--bun-light)"/>
          <stop offset="1" stop-color="var(--bun-dark)"/>
        </linearGradient>
      </defs>
      <rect x="10" y="150" width="900" height="330" rx="165" fill="url(#bunTone)" transform="rotate(-16 450 315)"/>
    </svg>

    <section class="contact">
      <span class="contact__label">Contact Us:</span>
      <span class="contact__phone">800-555-BMSC (2672)</span>
    </section>

    <p class="website">
      <svg class="website__icon" viewBox="0 0 24 24" fill="none" stroke="currentColor" stroke-width="1.5" aria-hidden="true">
        <circle cx="12" cy="12" r="10"/>
        <ellipse cx="12" cy="12" rx="4.5" ry="10"/>
        <line x1="2" y1="12" x2="22" y2="12"/>
        <path d="M4 7h16M4 17h16"/>
      </svg>
      brightmeadowsausage.com
    </p>
  </main>
</body>
</html>
```